Franchise Vacation Rental Company Website

We are looking for fresh, new and creative design ideas to help enhance this site. We are a vacation rental company that is starting a new franchise business. This will be our home franchise page, and will need to appeal to franchise candidates as well as travelers looking for vacation homes in our current locations.

Business

```html
<!DOCTYPE html>
<html lang="en">
<head>
<meta charset="utf-8">
<title>TideStays – Vacation Rental Services</title>
<link href="https://fonts.googleapis.com/css2?family=Ubuntu:wght@300;400;500&display=swap" rel="stylesheet">
<style>
:root{
  --green:#8cc63f;
  --green-soft:#7aab5a;
  --ink:#333;
  --muted:#8a8a8a;
  --field:#efefef;
  --footer:#1f1f1f;
  --footer-text:#9a9a9a;
  --white:#fff;
}
*{margin:0;padding:0;box-sizing:border-box}
html,body{width:725px;height:1200px;overflow:hidden;background:var(--white)}
body{position:relative;font-family:'Ubuntu',sans-serif;color:var(--ink)}
.abs{position:absolute}

.brand{left:88px;top:20px;font-size:16px;color:var(--green);font-weight:400}
.nav{left:266px;top:23px;width:368px;height:24px;border-bottom:2px solid var(--green);display:flex;font-size:7.5px;color:var(--muted)}
.nav a{text-decoration:none;color:inherit;display:block;padding-top:8px}
.nav .active{background:var(--green);color:var(--white);width:49px;text-align:center;padding-top:10px}
.nav .item{margin-left:auto}

.hero{left:0;top:47px;width:725px;height:254px;background:linear-gradient(180deg,#3f6fb0 0%,#7fa2cf 30%,#3f6a3a 52%,#e8ebee 66%,#5b6a68 78%,#2e4150 100%)}
.hero-tag{background:var(--green-soft);color:var(--white);font-weight:300}
.tag-main{left:417px;top:93px;width:104px;height:25px;font-size:17px;padding:3px 0 0 7px}
.tag-sub{left:417px;top:118px;width:129px;height:22px;font-size:10px;padding:5px 0 0 7px}

.search-title{left:157px;top:364px;font-size:16px;color:var(--green);font-weight:300}
.field{left:149px;width:119px;height:19px;background:var(--field);border:1px solid #e3e3e3;font-size:7px;color:var(--muted);padding:5px 0 0 8px}
.btn{background:var(--green);color:var(--white);font-size:8px;text-align:center}
.search-btn{left:149px;top:440px;width:119px;height:19px;padding-top:5px}

.spot{width:146px;height:120px}
.photo-harbour{background:linear-gradient(180deg,#2a4f9c 0%,#4d73b8 45%,#e9eef2 70%,#2c3e58 100%)}
.photo-island{background:linear-gradient(180deg,#eaf3f5 0%,#cfe0e2 35%,#5d8a4c 55%,#bfc7c5 75%,#6e8f58 100%)}
.photo-marina{background:linear-gradient(180deg,#3f78c9 0%,#cfe0f0 40%,#4f5c4e 65%,#2f4a2a 100%)}
.spot-label{width:132px;height:27px;font-size:8px;padding-top:9px}

.signup{left:132px;top:673px;width:454px;height:51px;border:1px solid #e6e6e6;background:var(--white);box-shadow:0 8px 6px -6px rgba(0,0,0,.25)}
.signup-text{left:156px;top:692px;font-size:9.5px;color:#555}
.email-field{left:314px;top:688px;width:161px;height:21px;background:var(--field);border:1px solid #e3e3e3;font-size:7px;color:var(--muted);padding:6px 0 0 10px}
.submit{left:484px;top:688px;width:78px;height:21px;padding-top:6px;font-size:7.5px}

.feature{width:120px;text-align:center}
.feature h3{font-size:9.5px;font-weight:400;margin-bottom:9px}
.feature svg{display:block;margin:0 auto}
.feature p{font-size:6.2px;line-height:7.8px;margin-top:17px;color:#444}

.footer{left:0;top:952px;width:725px;height:238px;background:var(--footer)}
.footer-rule{left:0;top:1149px;width:725px;height:1px;background:#333}
.footer h4{font-size:10.5px;font-weight:300;color:#bbb;margin-bottom:11px}
.footer-col{top:996px;font-size:7.5px;color:var(--footer-text);line-height:14px}
.contact-line{display:flex;align-items:center;gap:7px;margin-bottom:5px}
.social{display:flex;gap:4px}
.social span{width:21px;height:21px;display:block}
.copyright{left:0;top:1167px;width:725px;text-align:center;font-size:6px;color:#bbb}
</style>
</head>
<body>

<header>
  <div class="abs brand">TideStays</div>
  <nav class="abs nav">
    <a class="active" href="#">Home</a>
    <a class="item" style="margin-left:20px" href="#">Spots</a>
    <a style="margin-left:24px" href="#">Franchise</a>
    <a style="margin-left:28px" href="#">List Properties</a>
    <a style="margin-left:23px" href="#">Rentals</a>
    <a style="margin-left:24px" href="#">News</a>
    <a style="margin-left:22px" href="#">Contact</a>
  </nav>
</header>

<section>
  <div class="abs hero" role="img" aria-label="Harbour photo with moored white fishing boats, wooden pilings and waterfront houses among trees"></div>
  <div class="abs hero-tag tag-main">Vacation</div>
  <div class="abs hero-tag tag-sub">Rental Services</div>
</section>

<section>
  <h2 class="abs search-title" style="font-weight:300">Search Rentals</h2>
  <div class="abs field" style="top:394px">Destination</div>
  <div class="abs field" style="top:416px">Room</div>
  <div class="abs btn search-btn">Search</div>

  <div class="abs spot photo-harbour" style="left:290px;top:348px" role="img" aria-label="Photo of sailing boat masts in a harbour"></div>
  <div class="abs btn spot-label" style="left:297px;top:455px">Maryland Eastern Shore</div>
  <div class="abs spot photo-island" style="left:444px;top:348px" role="img" aria-label="Photo of a castle island across the bay"></div>
  <div class="abs btn spot-label" style="left:451px;top:455px">Maryland Eastern Shore</div>

  <div class="abs spot photo-marina" style="left:136px;top:491px" role="img" aria-label="Photo of a marina under blue sky with clouds"></div>
  <div class="abs btn spot-label" style="left:143px;top:598px">Maryland Eastern Shore</div>
  <div class="abs spot photo-island" style="left:290px;top:491px" role="img" aria-label="Photo of a castle island across the bay"></div>
  <div class="abs btn spot-label" style="left:297px;top:598px">Maryland Eastern Shore</div>
  <div class="abs spot photo-marina" style="left:444px;top:491px" role="img" aria-label="Photo of a marina under blue sky with clouds"></div>
  <div class="abs btn spot-label" style="left:451px;top:598px">Maryland Eastern Shore</div>
</section>

<section>
  <div class="abs signup"></div>
  <div class="abs signup-text">Signup for last getaway deals</div>
  <div class="abs email-field">Enter Your email</div>
  <div class="abs btn submit">Submit</div>
</section>

<section>
  <div class="abs feature" style="left:146px;top:771px">
    <h3>Great Spot</h3>
    <svg width="60" height="70" viewBox="0 0 60 70">
      <circle cx="30" cy="27" r="27" fill="#8cc63f"/>
      <path d="M30 18a6 6 0 0 1 6 6c0 5-6 11-6 11s-6-6-6-11a6 6 0 0 1 6-6z" fill="#fff"/>
      <circle cx="30" cy="24" r="2.3" fill="#8cc63f"/>
      <line x1="30" y1="54" x2="30" y2="66" stroke="#b8860b" stroke-width="1"/>
      <path d="M28 65l2 3 2-3z" fill="#6a8a2a"/>
    </svg>
    <p>Lorem ipsum dolor sit<br>amet this is a dummy texts lorem<br>ipsum dolor sit amet</p>
  </div>
  <div class="abs feature" style="left:293px;top:771px">
    <h3>Spot Travels free</h3>
    <svg width="60" height="70" viewBox="0 0 60 70">
      <circle cx="30" cy="27" r="27" fill="#8cc63f"/>
      <ellipse cx="30" cy="30" rx="4.5" ry="7" fill="#fff"/>
      <circle cx="26" cy="19" r="1.6" fill="#fff"/>
      <circle cx="29.5" cy="18" r="1.4" fill="#fff"/>
      <circle cx="32.5" cy="18.6" r="1.2" fill="#fff"/>
      <circle cx="34.8" cy="20.2" r="1" fill="#fff"/>
      <line x1="30" y1="54" x2="30" y2="66" stroke="#b8860b" stroke-width="1"/>
      <path d="M28 65l2 3 2-3z" fill="#6a8a2a"/>
    </svg>
    <p>Lorem ipsum dolor sit<br>amet this is a dummy texts lorem<br>ipsum dolor sit amet</p>
  </div>
  <div class="abs feature" style="left:442px;top:771px">
    <h3>Last Min Deads</h3>
    <svg width="60" height="70" viewBox="0 0 60 70">
      <circle cx="30" cy="27" r="27" fill="#8cc63f"/>
      <circle cx="30" cy="27" r="8" fill="none" stroke="#fff" stroke-width="1.6"/>
      <path d="M30 22v5h-3.5" fill="none" stroke="#fff" stroke-width="1.6"/>
      <line x1="30" y1="54" x2="30" y2="66" stroke="#b8860b" stroke-width="1"/>
      <path d="M28 65l2 3 2-3z" fill="#6a8a2a"/>
    </svg>
    <p>Lorem ipsum dolor sit<br>amet this is a dummy texts lorem<br>ipsum dolor sit amet</p>
  </div>
</section>

<footer>
  <div class="abs footer"></div>
  <div class="abs footer footer-col" style="left:132px;top:996px;width:140px;height:auto;background:none">
    <h4>Know More About US</h4>
    <div>Who we are?</div>
    <div>What we do?</div>
    <div>Franchise information</div>
    <div>Our Philosophy</div>
  </div>
  <div class="abs footer footer-col" style="left:305px;top:996px;width:150px;height:auto;background:none">
    <h4>Contact Us</h4>
    <div class="contact-line">
      <svg width="9" height="9" viewBox="0 0 24 24"><path d="M6.6 10.8a15 15 0 0 0 6.6 6.6l2.2-2.2c.3-.3.7-.4 1-.2 1.1.4 2.3.6 3.6.6.6 0 1 .4 1 1V20c0 .6-.4 1-1 1A17 17 0 0 1 3 4c0-.6.4-1 1-1h3.5c.6 0 1 .4 1 1 0 1.3.2 2.5.6 3.6.1.3 0 .7-.2 1z" fill="#9a9a9a"/></svg>
      <span>+1 555 014 2887</span>
    </div>
    <div class="contact-line">
      <svg width="9" height="8" viewBox="0 0 24 20"><path d="M2 2h20v16H2z" fill="#9a9a9a"/><path d="M2 3l10 8 10-8" fill="none" stroke="#1f1f1f" stroke-width="2"/></svg>
      <span>hello@tidestays.example</span>
    </div>
  </div>
  <div class="abs footer footer-col" style="left:461px;top:996px;width:140px;height:auto;background:none">
    <h4>Find us on</h4>
    <div class="social">
      <span style="background:#3b5a9a" aria-label="Social profile"></span>
      <span style="background:#2aa3dc" aria-label="Social profile"></span>
      <span style="background:#d3222a" aria-label="Social profile"></span>
      <span style="background:#1a7fb0" aria-label="Social profile"></span>
      <span style="background:#e04a3b" aria-label="Social profile"></span>
    </div>
  </div>
  <div class="abs footer-rule"></div>
  <div class="abs copyright">Copyright note@tidestays.example</div>
</footer>

</body>
</html>
```